TECH PROJECT NEEDS NEW SKINS FOR RE-BRANDING

We are a technology project that has a product (crypto wallet) nearing release, have basic designs made so far however we need NEW SKINS/ branding/ design options for this wallet to change the look and feel -- it will be called and re-branded as "KESTROL" a futuristic/ space/ edgy product so need it to look like so.

YOU ARE ALLOWED TO CHANGE + EXPERIMENT WITH THE LAYOUT/ schema and UI as you see fit -- (we are open to new and creative ideas)

(see WALLET.PNG and PROTFOLIO.PNG ATTACHED --- these are the pages we need new skins for )

(see KESTROL logo attached --- PLEASE USE THIS LOGO/ VERSIONS OF THIS LOGO IN YOUR DESIGNS/SKIN SUBMISSIONS -- WE PROVIDED THE ai file so feel free to alter the logo a bit to experiment if you want -- we are open and flexible to new creative ideas)

(FOR A MOOD BOARD FOR GUIDANCE on feel/colors/mood-- SEE "SAMPLE INTERFACE 1 & 2" ATTACHED)

Target Market(s)

TECHNOLOGY/SPACE/ FUTURE

Number of Pages Required

2 page

Colors

Designer to choose colors to be used in the design.

Requirements
Must have
• MUST USE OUR KESTROL LOGO OR A SIMILAR ALTERATION OF IT

```html
<!DOCTYPE html>
<html lang="en">
<head>
<meta charset="utf-8">
<title>KESTROL Wallet &amp; Portfolio</title>
<link href="https://fonts.googleapis.com/css2?family=Roboto:wght@400;500;700&family=Roboto+Condensed:wght@400;700&display=swap" rel="stylesheet">
<style>
:root{
  --stage-a:#0e2e38;--stage-b:#174a55;
  --screen:#0c1c2a;--side:#10293a;--main:#132d3e;--panel:#173a52;--panel-dark:#0b1826;
  --line:#2a5a6e;--line-soft:#1f4456;--blue:#2a7ff0;--blue-dark:#0f2d63;
  --orange:#e8642a;--teal:#2fd0b0;--teal-btn:#1d6e62;--text:#e6eef3;--muted:#8aa3b3;
  --tab:#1c3a4c;--tab-active:#d7dde2;
  --slr:#e8642a;--vxa:#2a8fe0;--aet:#7b3df0;--lnr:#9aa6ae;--qvr:#4a8fe8;--nbl:#2a6ee8;
}
*{box-sizing:border-box;margin:0;padding:0}
html,body{width:1200px;height:1200px;overflow:hidden}
body{background:radial-gradient(circle at 50% 40%,var(--stage-b),var(--stage-a) 75%);font-family:"Roboto",sans-serif;color:var(--text);position:relative}
.screen{position:absolute;background:var(--screen);overflow:hidden;box-shadow:0 20px 50px rgba(0,0,0,.45)}
.screen--wallet{left:80px;top:80px;width:884px;height:498px}
.screen--portfolio{left:236px;top:622px;width:882px;height:496px;background:var(--main)}
/* sidebar */
.sidebar{position:absolute;left:0;top:0;width:74px;height:100%;background:var(--side);border-right:1px solid var(--line)}
.brand{position:absolute;top:20px;left:0;width:74px;text-align:center}
.brand-dot{width:14px;height:14px;border:2px solid var(--text);border-radius:50%;margin:0 auto 4px}
.brand-name{font-size:9px;font-weight:500;letter-spacing:1px}
.nav-tab{position:absolute;left:0;width:65px;height:52px;background:var(--tab);clip-path:polygon(0 0,82% 0,100% 22%,100% 100%,0 100%);text-align:center;font-size:7.5px;font-weight:500;padding-top:7px}
.nav-tab svg{display:block;margin:0 auto 4px;width:18px;height:18px;stroke:#c9d6de;fill:none;stroke-width:1.3}
.nav-tab--active{background:var(--tab-active);color:#1a2a36}
.nav-tab--active svg{stroke:var(--orange)}
.nav-tab--settings{background:var(--panel-dark);padding-top:16px}
/* generic */
.search{position:absolute;border-bottom:1px solid var(--orange);background:var(--panel-dark);font-size:7.5px;color:var(--orange);padding:8px 6px 0}
.search svg{position:absolute;right:6px;top:6px;width:11px;height:11px;stroke:var(--orange);fill:none;stroke-width:1.4}
.coin-dot{width:16px;height:16px;border-radius:50%;border:1.5px solid currentColor;flex:none;background:rgba(255,255,255,.06)}
.c-slr{color:var(--slr)}.c-vxa{color:var(--vxa)}.c-aet{color:var(--aet)}.c-lnr{color:var(--lnr)}.c-qvr{color:var(--qvr)}.c-nbl{color:var(--nbl)}
/* wallet list */
.wallet-col{position:absolute;left:74px;top:0;width:220px;height:100%;background:#0b1a28;border-right:1px solid var(--line)}
.page-title{position:absolute;font-family:"Roboto Condensed",sans-serif;font-weight:700;font-size:18px;letter-spacing:.3px}
.list-frame{position:absolute;left:17px;top:80px;width:187px;height:344px;border:1px solid var(--line-soft)}
.coin-item{position:absolute;left:36px;width:150px;height:32px;border:1px solid var(--line-soft);background:#0d1f2e;display:flex;align-items:center;gap:8px;padding-left:4px}
.coin-item--active{background:var(--blue-dark);border-color:var(--blue)}
.coin-name{font-size:7px;font-weight:500}
.coin-amt{font-size:7px;color:var(--muted);margin-top:3px}
/* wallet main */
.wallet-main{position:absolute;left:294px;top:0;right:0;height:100%;background:var(--main)}
.asset-head{position:absolute;left:20px;top:16px;width:550px;height:46px;border:1px solid var(--blue);background:#123055;display:flex;align-items:center;padding-left:12px}
.asset-head .coin-dot{width:22px;height:22px}
.asset-head h1{font-family:"Roboto Condensed",sans-serif;font-size:19px;font-weight:700;color:var(--blue);margin-left:14px}
.asset-head h1 span{color:var(--text)}
.rate{position:absolute;right:10px;top:10px;width:196px;height:28px;background:var(--panel-dark);font-size:7px;text-align:right;padding:10px 8px 0 0}
.band{position:absolute;left:0;right:0;height:1px;background:var(--line-soft)}
.balance{position:absolute;left:20px;top:94px;width:312px;height:119px;background:var(--panel);border:1px solid var(--line-soft);padding:10px 14px}
.label{font-size:7px;color:var(--blue)}
.balance-box{margin-top:5px;height:39px;background:var(--panel-dark);border:1px solid var(--blue);padding:5px 9px}
.balance-box b{font-size:15px;font-weight:500}
.balance-box div{font-size:7.5px;color:var(--blue);margin-top:3px}
.addr{display:flex;justify-content:space-between;font-size:7px;margin-top:4px}
.addr em{font-style:normal;color:var(--orange)}
.actions{position:absolute;left:356px;top:94px;width:212px;height:118px;background:#1c3e52;border:1px solid var(--line-soft)}
.act-btn{position:absolute;top:13px;width:91px;height:52px;font-size:8px;font-weight:700;text-align:center;padding-top:8px}
.act-btn svg{display:block;margin:6px auto 0;width:20px;height:22px;fill:none;stroke:currentColor;stroke-width:1.3}
.act-send{left:9px;background:#9aa7ae;color:#e8eef2;clip-path:polygon(0 0,100% 0,100% 75%,85% 100%,0 100%)}
.act-recv{left:104px;border:1px solid #cfd8de;color:var(--text)}
.actions .search{left:9px;top:77px;width:194px;height:26px}
.tx-table{position:absolute;left:20px;top:243px;width:546px}
.tx-head{height:39px;border:1px solid var(--teal-btn);display:grid;grid-template-columns:94px 46px 108px 63px 67px 105px 1fr;align-items:center;padding-left:10px;font-size:7px;color:var(--muted)}
.tx-row{height:26px;margin-top:6.5px;background:#26404f;display:grid;grid-template-columns:94px 46px 108px 63px 67px 105px 1fr;align-items:center;padding-left:4px;font-size:7px}
.tx-row:first-of-type{margin-top:7px}
.tx-row--alt{background:#1d3b4a}
.tx-act{display:flex;align-items:center;gap:5px}
.tx-act i{width:13px;height:13px;border:1px solid #cfd8de;border-radius:50%;display:block}
.tx-row--alt .tx-act{color:var(--teal)}
.tx-row--alt .tx-act i{border-color:var(--teal)}
.s-pend{color:var(--orange)}.s-ok{color:var(--teal)}
.details{width:52px;height:18px;background:var(--teal-btn);border:1px solid var(--teal);color:var(--teal);font-size:7px;text-align:center;line-height:17px}
/* portfolio */
.pf-side{background:var(--side)}
.pf-rail{position:absolute;left:74px;top:0;width:24px;height:100%;background:#0f2636;border-right:1px solid var(--line)}
.pf-head{position:absolute;left:98px;right:0;top:0;height:70px;background:#0f2636;border-bottom:1px solid var(--line)}
.select{position:absolute;left:566px;top:18px;width:134px;height:25px;border-bottom:1px solid var(--orange);background:var(--panel-dark);font-size:7.5px;color:var(--orange);padding:8px 6px 0}
.select svg{position:absolute;right:8px;top:10px;width:10px;height:6px;stroke:var(--orange);fill:none}
.add-btn{position:absolute;left:727px;top:18px;width:138px;height:37px;background:#5d6b73;border:1px solid #aab5bb;font-size:8px;font-weight:700;text-align:center;line-height:36px;clip-path:polygon(0 0,100% 0,100% 100%,12% 100%,0 70%)}
.est{position:absolute;left:114px;top:83px;width:260px;height:72px;background:var(--panel);border:1px solid var(--line-soft);padding:9px 14px}
.est-box{margin-top:4px;height:24px;background:var(--panel-dark);font-size:15px;font-weight:500;padding:3px 6px}
.est small{display:block;font-size:7px;margin-top:6px}
.range{position:absolute;top:106px;width:79px;height:27px;font-size:8.5px;font-weight:700;text-align:center;line-height:27px;border:1px solid #9fb0ba;clip-path:polygon(16% 0,100% 0,100% 100%,0 100%,0 70%)}
.range--on{background:#dfe4e7;color:#1a2a36;border:none;clip-path:polygon(0 0,100% 0,100% 30%,84% 100%,0 100%)}
.cards{position:absolute;left:114px;top:170px;width:751px;height:53px;border:1px solid var(--line-soft);border-top:none;border-bottom:none}
.card{position:absolute;top:8px;width:117px;height:36px;display:flex;align-items:center;gap:8px;padding-left:6px}
.card .coin-name{font-size:7px}
.stats{position:absolute;left:114px;top:231px;width:751px;height:39px;border:1px solid var(--line-soft);border-top:none;display:grid;grid-template-columns:repeat(6,1fr)}
.stat{padding:9px 6px 0 20px;position:relative}
.stat .label{font-size:7px}
.stat b{display:block;font-size:8.5px;margin-top:4px}
.stat em{position:absolute;right:6px;top:8px;font-style:normal;font-size:6px;text-align:center;color:var(--teal);line-height:8px}
.stat em.down{color:var(--orange)}
.pf-table{position:absolute;left:114px;top:299px;width:751px}
.pf-headrow{height:38px;border:1px solid var(--line-soft);display:grid;grid-template-columns:140px 73px 69px 69px 75px 88px 88px 64px 1fr;align-items:center;padding-left:26px;font-size:7px;color:var(--muted)}
.pf-row{height:26px;margin-top:6px;display:grid;grid-template-columns:140px 73px 69px 69px 75px 88px 88px 64px 1fr;align-items:center;padding-left:20px;font-size:7px;border-left:2px solid currentColor}
.pf-row:first-of-type{margin-top:8px}
.pf-cell{color:var(--text)}
.pf-name{display:flex;align-items:center;gap:8px}
.pf-name .coin-dot{width:15px;height:15px}
.pf-name .pf-label{color:inherit}
.pf-name .pf-label--plain{color:var(--text)}
.chg{color:var(--teal)}.chg.down{color:var(--orange)}
.btns{display:flex;gap:6px}
.btn-send{width:29px;height:18px;background:#6d7a82;border:1px solid #aab5bb;text-align:center;line-height:17px;font-size:7px;color:var(--text)}
.btn-recv{width:42px;height:18px;border:1px solid #cfd8de;text-align:center;line-height:17px;font-size:7px;background:#0f1e2a;color:var(--text)}
.bg-slr{background:linear-gradient(90deg,#4a2a22,#2b2f36)}
.bg-vxa{background:linear-gradient(90deg,#123d63,#15324a)}
.bg-aet{background:linear-gradient(90deg,#2c1c63,#221e4e)}
.bg-lnr{background:#243844}
.bg-qvr{background:linear-gradient(90deg,#163a60,#15324a)}
.bg-nbl{background:#10294f}
</style>
</head>
<body>

<!-- Wallet screen -->
<section class="screen screen--wallet" aria-label="Wallet">
  <nav class="sidebar">
    <div class="brand"><div class="brand-dot"></div><div class="brand-name">KESTROL</div></div>
    <div class="nav-tab" style="top:80px"><svg viewBox="0 0 18 18"><rect x="2" y="2" width="6" height="6"/><rect x="10" y="2" width="6" height="6"/><rect x="2" y="10" width="6" height="6"/><rect x="10" y="10" width="6" height="6"/></svg>Dashboard</div>
    <div class="nav-tab" style="top:138px"><svg viewBox="0 0 18 18"><path d="M2 2v14h14M4 12l4-4 3 3 5-6"/></svg>Portfolio</div>
    <div class="nav-tab nav-tab--active" style="top:198px"><svg viewBox="0 0 18 18"><rect x="3" y="4" width="12" height="11" fill="#e8642a"/></svg>Wallet</div>
    <div class="nav-tab" style="top:256px"><svg viewBox="0 0 18 18"><path d="M11 1L4 10h5l-2 7 7-9H9z"/></svg>Lightning</div>
    <div class="nav-tab" style="top:318px"><svg viewBox="0 0 18 18"><path d="M4 13h10a3 3 0 0 0 0-6 4 4 0 0 0-8-1 3.5 3.5 0 0 0-2 7z"/></svg>NBL Cloud</div>
    <div class="nav-tab nav-tab--settings" style="top:378px"><svg viewBox="0 0 18 18"><circle cx="9" cy="9" r="6" stroke-dasharray="2.5 1.5"/><circle cx="9" cy="9" r="2.5"/></svg></div>
  </nav>

  <aside class="wallet-col">
    <h1 class="page-title" style="left:40px;top:34px">WALLET</h1>
    <div class="list-frame"></div>
    <div class="search" style="left:36px;top:112px;width:150px;height:24px">Search...<svg viewBox="0 0 12 12"><circle cx="5" cy="5" r="3.5"/><path d="M8 8l3 3"/></svg></div>
    <div class="coin-item" style="top:153px"><span class="coin-dot c-slr"></span><div><div class="coin-name c-slr">Solarin - SLR</div><div class="coin-amt">369,800.00 SLR</div></div></div>
    <div class="coin-item" style="top:194px"><span class="coin-dot c-vxa"></span><div><div class="coin-name c-vxa">Vexa - VXA</div><div class="coin-amt">369,800.00 VXA</div></div></div>
    <div class="coin-item" style="top:234px"><span class="coin-dot c-aet"></span><div><div class="coin-name c-aet">Aethon - AET</div><div class="coin-amt">369,800.00 AET</div></div></div>
    <div class="coin-item" style="top:275px"><span class="coin-dot c-lnr"></span><div><div class="coin-name">Lunaris - LNR</div><div class="coin-amt">369,800.00 LNR</div></div></div>
    <div class="coin-item" style="top:316px"><span class="coin-dot c-qvr"></span><div><div class="coin-name c-qvr">Quiver - QVR</div><div class="coin-amt">369,800.00 QVR</div></div></div>
    <div class="coin-item coin-item--active" style="top:358px"><span class="coin-dot c-nbl"></span><div><div class="coin-name">Nebulon - NBL</div><div class="coin-amt">369,800.00 NBL</div></div></div>
  </aside>

  <main class="wallet-main">
    <header class="asset-head"><span class="coin-dot c-nbl"></span><h1>Nebulon - <span>NBL</span></h1><div class="rate">1 NBL = 0.08 USD</div></header>
    <div class="band" style="top:80px"></div>
    <div class="balance">
      <div class="label">Balance</div>
      <div class="balance-box"><b>369.000 NBL</b><div>= 29.584.00 USD</div></div>
      <div class="label" style="margin-top:12px">Wallet Address</div>
      <div class="addr"><span>TgjkbLN m27g3 lkkkBkLkJgbk</span><em>Copy</em></div>
    </div>
    <div class="actions">
      <div class="act-btn act-send">SEND MONEY<svg viewBox="0 0 20 22"><path d="M10 1l8 5v10l-8 5-8-5V6z"/><path d="M10 16V7M6 10l4-4 4 4"/></svg></div>
      <div class="act-btn act-recv">RECEIVE MONEY<svg viewBox="0 0 20 22"><path d="M10 1l8 5v10l-8 5-8-5V6z"/><path d="M10 6v9M6 12l4 4 4-4"/></svg></div>
      <div class="search">Search...<svg viewBox="0 0 12 12"><circle cx="5" cy="5" r="3.5"/><path d="M8 8l3 3"/></svg></div>
    </div>
    <div class="band" style="top:228px"></div>
    <div class="tx-table">
      <div class="tx-head"><span>ACTIVITY</span><span>DATE</span><span>TRANSACTION ID</span><span>AMOUNT</span><span>STATUS</span><span>BALANCE CHANGE</span><span style="padding-left:8px">DETAILS</span></div>
      <div class="tx-row"><span class="tx-act"><i></i>Sending Money</span><span>11.03.19</span><span>TgjkbLN m27ggvKhn637d...</span><span>43.00 NBL</span><span class="s-pend">Pending</span><span>369,800.00 NBL</span><span class="details">DETAILS</span></div>
      <div class="tx-row tx-row--alt"><span class="tx-act"><i></i>Receiving Money</span><span>11.03.19</span><span>TgjkbLN m27ggvKhn637d...</span><span>43.00 NBL</span><span class="s-ok">Success</span><span>369,800.00 NBL</span><span class="details">DETAILS</span></div>
      <div class="tx-row"><span class="tx-act"><i></i>Sending Money</span><span>11.03.19</span><span>TgjkbLN m27ggvKhn637d...</span><span>43.00 NBL</span><span class="s-ok">Success</span><span>369,800.00 NBL</span><span class="details">DETAILS</span></div>
      <div class="tx-row tx-row--alt"><span class="tx-act"><i></i>Receiving Money</span><span>11.03.19</span><span>TgjkbLN m27ggvKhn637d...</span><span>43.00 NBL</span><span class="s-pend">Pending</span><span>369,800.00 NBL</span><span class="details">DETAILS</span></div>
      <div class="tx-row"><span class="tx-act"><i></i>Sending Money</span><span>11.03.19</span><span>TgjkbLN m27ggvKhn637d...</span><span>43.00 NBL</span><span class="s-ok">Success</span><span>369,800.00 NBL</span><span class="details">DETAILS</span></div>
      <div class="tx-row tx-row--alt"><span class="tx-act"><i></i>Receiving Money</span><span>11.03.19</span><span>TgjkbLN m27ggvKhn637d...</span><span>43.00 NBL</span><span class="s-ok">Success</span><span>369,800.00 NBL</span><span class="details">DETAILS</span></div>
      <div class="tx-row tx-row--alt"><span class="tx-act"><i></i>Receiving Money</span><span>11.03.19</span><span>TgjkbLN m27ggvKhn637d...</span><span>43.00 NBL</span><span class="s-ok">Success</span><span>369,800.00 NBL</span><span class="details">DETAILS</span></div>
    </div>
  </main>
</section>

<!-- Portfolio screen -->
<section class="screen screen--portfolio" aria-label="Portfolio">
  <nav class="sidebar pf-side">
    <div class="brand"><div class="brand-dot"></div><div class="brand-name">KESTROL</div></div>
    <div class="nav-tab" style="top:78px"><svg viewBox="0 0 18 18"><rect x="2" y="2" width="6" height="6"/><rect x="10" y="2" width="6" height="6"/><rect x="2" y="10" width="6" height="6"/><rect x="10" y="10" width="6" height="6"/></svg>Dashboard</div>
    <div class="nav-tab nav-tab--active" style="top:138px"><svg viewBox="0 0 18 18"><path d="M2 2v14h14M4 12l4-4 3 3 5-6"/></svg>Portfolio</div>
    <div class="nav-tab" style="top:196px"><svg viewBox="0 0 18 18"><rect x="3" y="4" width="12" height="11"/></svg>Wallet</div>
    <div class="nav-tab" style="top:255px"><svg viewBox="0 0 18 18"><path d="M11 1L4 10h5l-2 7 7-9H9z"/></svg>Lightning</div>
    <div class="nav-tab" style="top:316px"><svg viewBox="0 0 18 18"><path d="M4 13h10a3 3 0 0 0 0-6 4 4 0 0 0-8-1 3.5 3.5 0 0 0-2 7z"/></svg>NBL Cloud</div>
    <div class="nav-tab nav-tab--settings" style="top:378px"><svg viewBox="0 0 18 18"><circle cx="9" cy="9" r="6" stroke-dasharray="2.5 1.5"/><circle cx="9" cy="9" r="2.5"/></svg></div>
  </nav>
  <div class="pf-rail"></div>
  <header class="pf-head"></header>
  <h1 class="page-title" style="left:118px;top:24px">PORTOFLIO</h1>
  <div class="search" style="left:272px;top:18px;width:284px;height:25px">Search...<svg viewBox="0 0 12 12"><circle cx="5" cy="5" r="3.5"/><path d="M8 8l3 3"/></svg></div>
  <div class="select">All<svg viewBox="0 0 10 6"><path d="M0 0l5 5 5-5z"/></svg></div>
  <div class="add-btn">+ ADD TRANSACTION</div>

  <div class="est"><div class="label">Est. Assets Value</div><div class="est-box">$ 1,270,000.98</div><small>6 Assets</small></div>
  <div class="range range--on" style="left:412px">24 H</div>
  <div class="range" style="left:506px">WEEK</div>
  <div class="range" style="left:598px">MONTH</div>
  <div class="range" style="left:692px">YEAR</div>
  <div class="range" style="left:786px">ALL</div>

  <div class="cards">
    <div class="card bg-slr" style="left:13px"><span class="coin-dot c-slr"></span><div><div class="coin-name c-slr">Solarin - SLR</div><div class="coin-amt">444,800.00 SLR</div></div></div>
    <div class="card bg-vxa" style="left:135px"><span class="coin-dot c-vxa"></span><div><div class="coin-name c-vxa">Vexa - VXA</div><div class="coin-amt">45,800.00 VXA</div></div></div>
    <div class="card bg-aet" style="left:257px"><span class="coin-dot c-aet"></span><div><div class="coin-name c-aet">Aethon - AET</div><div class="coin-amt">289,800.00 AET</div></div></div>
    <div class="card bg-lnr" style="left:378px"><span class="coin-dot c-lnr"></span><div><div class="coin-name">Lunaris - LNR</div><div class="coin-amt">330,800.00 LNR</div></div></div>
    <div class="card bg-qvr" style="left:500px"><span class="coin-dot c-qvr"></span><div><div class="coin-name c-qvr">Quiver - QVR</div><div class="coin-amt">355,800.00 QVR</div></div></div>
    <div class="card bg-nbl" style="left:621px"><span class="coin-dot c-nbl"></span><div><div class="coin-name">Nebulon - NBL</div><div class="coin-amt">369,800.00 NBL</div></div></div>
  </div>

  <div class="stats">
    <div class="stat"><div class="label">Portfolio Change</div><b>$ 1.234.100,89</b><em>↑<br>36.9%</em></div>
    <div class="stat"><div class="label">Profit/ Loss</div><b>$ 1.234.100,89</b><em>↑<br>36.9%</em></div>
    <div class="stat"><div class="label">24H Profit/ Loss</div><b>$ 1.234.100,89</b><em>↑<br>36.9%</em></div>
    <div class="stat"><div class="label">Best Assets</div><b>Nebulon - NBL</b><em>↑<br>36.9%</em></div>
    <div class="stat"><div class="label">Worst Assets</div><b>Solarin - SLR</b><em class="down">↓<br>36.9%</em></div>
    <div class="stat"><div class="label">Portfolio Age</div><b>6M 24D 3H</b></div>
  </div>
  <div class="band" style="top:284px;left:98px"></div>

  <div class="pf-table">
    <div class="pf-headrow"><span>ASSET NAME</span><span>MARKET CAP</span><span>VOLUME 24H</span><span>% CHANGE</span><span>LAST PRICE</span><span>BALANCE</span><span>VALUE</span><span>PORTFOLIO</span><span>ACTIONS</span></div>
    <div class="pf-row bg-slr c-slr"><span class="pf-name"><span class="coin-dot"></span><span class="pf-label">Solarin - SLR</span></span><span class="pf-cell">120 B</span><span class="pf-cell">2,7 B</span><span class="chg down">↓ 36.9%</span><span class="pf-cell">$ 3,666.99</span><span class="pf-cell">$ 1,270,000.98</span><span class="pf-cell">369,800.00 NBL</span><span class="pf-cell">12.7%</span><span class="btns"><span class="btn-send">SEND</span><span class="btn-recv">RECEIVE</span></span></div>
    <div class="pf-row bg-vxa c-vxa"><span class="pf-name"><span class="coin-dot"></span><span class="pf-label">Vexa - VXA</span></span><span class="pf-cell">30 B</span><span class="pf-cell">2,7 B</span><span class="chg">↑ 36.9%</span><span class="pf-cell">$ 3,666.99</span><span class="pf-cell">$ 1,270,000.98</span><span class="pf-cell">369,800.00 NBL</span><span class="pf-cell">12,7%</span><span class="btns"><span class="btn-send">SEND</span><span class="btn-recv">RECEIVE</span></span></div>
    <div class="pf-row bg-aet c-aet"><span class="pf-name"><span class="coin-dot"></span><span class="pf-label">Aethon - AET</span></span><span class="pf-cell">30 B</span><span class="pf-cell">2,7 B</span><span class="chg">↑ 36.9%</span><span class="pf-cell">$ 3,666.99</span><span class="pf-cell">$ 1,270,000.98</span><span class="pf-cell">369,800.00 NBL</span><span class="pf-cell">12,7%</span><span class="btns"><span class="btn-send">SEND</span><span class="btn-recv">RECEIVE</span></span></div>
    <div class="pf-row bg-lnr c-lnr"><span class="pf-name"><span class="coin-dot"></span><span class="pf-label pf-label--plain">Lunaris - LNR</span></span><span class="pf-cell">30 B</span><span class="pf-cell">2,7 B</span><span class="chg">↑ 36.9%</span><span class="pf-cell">$ 3,666.99</span><span class="pf-cell">$ 1,270,000.98</span><span class="pf-cell">369,800.00 NBL</span><span class="pf-cell">12,7%</span><span class="btns"><span class="btn-send">SEND</span><span class="btn-recv">RECEIVE</span></span></div>
    <div class="pf-row bg-qvr c-qvr"><span class="pf-name"><span class="coin-dot"></span><span class="pf-label">Quiver - QVR</span></span><span class="pf-cell">30 B</span><span class="pf-cell">2,7 B</span><span class="chg">↑ 36.9%</span><span class="pf-cell">$ 3,666.99</span><span class="pf-cell">$ 1,270,000.98</span><span class="pf-cell">369,800.00 NBL</span><span class="pf-cell">12,7%</span><span class="btns"><span class="btn-send">SEND</span><span class="btn-recv">RECEIVE</span></span></div>
  </div>
</section>

</body>
</html>
```